"Vortexnova" Show on Trelvano and quibstar needs a thumbnail.

Hello, I need a thumbnail image for a new show I want to start Trelvano and Quibstar soon. This show represents different styles of music out of all EDM genres mixed to approx. one hour sets. Please find attached CD covers I really like in their style and which can be used as inspiration. This show should be released on a weekly basis. So I want to attach my logo which needs to be thumbnailed / image as well

Target Market(s)

Young EDM Lovers

Industry/Entity Type

Quibstar

Requirements
Must have
• The cover needs to have the above mentioned title in a cool lettering and the name of the artist (which can be found in the attached pictures in color and style. should represent electronic music.
Nice to have
• I imagine child of earth ball instead of speakers or symbols in the cover. It shall represent the (re-) union which happens when young people come together and share their passion for music. Does not matter which style it is. It's also nice to have a space for adding social media information on the thumbnail.
Should not have
• Should not be too colorful. No comic style.

```html
<!DOCTYPE html>
<html lang="en">
<head>
<meta charset="utf-8">
<title>Kestrava presents Vortexnova – Episode 001</title>
<link rel="stylesheet" href="https://fonts.googleapis.com/css2?family=Audiowide&family=Bebas+Neue&family=Orbitron:wght@700;900&display=swap">
<style>
  :root {
    --night: #04102e;
    --deep: #0a2a6e;
    --glow: #2f7fe0;
    --cyan: #2aa9f0;
    --white: #f4f7fb;
    --band: rgba(3, 10, 30, 0.78);
    --band-light: rgba(10, 26, 60, 0.72);
  }
  * { margin: 0; padding: 0; box-sizing: border-box; }
  html, body { width: 1200px; height: 674px; overflow: hidden; background: var(--night); }
  .thumbnail {
    position: relative;
    width: 1200px;
    height: 674px;
    overflow: hidden;
    color: var(--white);
    font-family: "Bebas Neue", sans-serif;
  }
  .backdrop {
    position: absolute; inset: 0;
    background:
      radial-gradient(ellipse 260px 300px at 600px 430px, rgba(60,130,230,0.55), transparent 75%),
      radial-gradient(circle 180px at 90px 90px, rgba(60,120,200,0.35), transparent 80%),
      radial-gradient(circle 200px at 1110px 90px, rgba(60,120,200,0.35), transparent 80%),
      radial-gradient(ellipse 700px 400px at 600px 300px, #1a4da8, transparent 80%),
      linear-gradient(180deg, #0c2f78 0%, #071c4c 55%, #041231 100%);
  }
  .brand {
    position: absolute; left: 356px; top: 69px; width: 485px; height: 80px;
    border-top: 4px solid var(--cyan);
    border-bottom: 4px solid var(--cyan);
    display: flex; align-items: center; justify-content: center;
  }
  .brand-name {
    font-family: "Orbitron", sans-serif; font-weight: 900;
    font-size: 46px; letter-spacing: 2px; color: var(--cyan);
  }
  .presents {
    position: absolute; left: 356px; top: 176px; width: 490px;
    display: flex; justify-content: space-between;
    font-family: "Orbitron", sans-serif; font-weight: 700; font-size: 28px;
    color: #dfe6ee;
  }
  .show-title {
    position: absolute; left: 0; top: 236px; width: 1200px; text-align: center;
    font-family: "Audiowide", sans-serif; font-size: 98px; letter-spacing: 6px;
    line-height: 1; color: var(--white);
    text-shadow: 0 3px 10px rgba(0,0,0,0.6);
  }
  .guest {
    position: absolute; left: 0; top: 362px; width: 1190px; text-align: center;
    line-height: 1; text-shadow: 0 2px 6px rgba(0,0,0,0.7);
  }
  .guest-label { font-family: "Orbitron", sans-serif; font-weight: 900; font-size: 29px; letter-spacing: 1px; }
  .guest-artist { font-size: 54px; margin-top: 4px; }
  .now-playing {
    position: absolute; left: 0; top: 453px; width: 216px; height: 36px;
    background: var(--band);
    clip-path: polygon(0 0, 100% 0, 88% 100%, 0 100%);
    font-size: 27px; line-height: 38px; padding-left: 42px;
  }
  .track {
    position: absolute; left: 0; top: 497px; width: 370px; height: 88px;
    background: var(--band-light);
    clip-path: polygon(0 0, 100% 0, 94% 100%, 0 100%);
    padding: 8px 0 0 16px; line-height: 1;
  }
  .track-title { font-size: 35px; }
  .track-artists { font-size: 27px; margin-top: 6px; }
  .episode {
    position: absolute; left: 528px; top: 551px; width: 136px; text-align: center;
    font-family: "Orbitron", sans-serif; font-weight: 900; line-height: 1;
    text-shadow: 0 2px 6px rgba(0,0,0,0.7);
  }
  .episode-label { font-size: 23px; }
  .episode-number { font-size: 54px; margin-top: 2px; }
  .socials {
    position: absolute; right: 0; top: 453px; width: 340px;
  }
  .social-row {
    display: flex; justify-content: space-between; align-items: center;
    height: 46px; padding: 0 8px 0 20px;
    background: var(--band-light);
    clip-path: polygon(4% 0, 100% 0, 100% 100%, 0 100%);
    margin-bottom: 4px;
  }
  .social { display: flex; align-items: center; gap: 6px; font-size: 23px; }
  .social-mark { width: 14px; height: 14px; background: var(--white); }
  .website {
    margin-left: 130px; height: 30px; padding-left: 32px;
    background: var(--band);
    clip-path: polygon(8% 0, 100% 0, 100% 100%, 0 100%);
    font-size: 25px; line-height: 32px;
  }
</style>
</head>
<body>
<main class="thumbnail">
  <div class="backdrop" role="img" aria-label="Glowing blue sphere of cubes with network lines, speakers and scrolling code in the background"></div>

  <header class="brand"><span class="brand-name">KESTRAVA</span></header>
  <div class="presents"><span>P</span><span>R</span><span>E</span><span>S</span><span>E</span><span>N</span><span>T</span><span>S</span></div>
  <h1 class="show-title">VORTEXNOVA</h1>

  <div class="guest">
    <div class="guest-label">GUEST MIX BY</div>
    <div class="guest-artist">ARTIST LOGO</div>
  </div>

  <div class="now-playing">NOW PLAYING</div>
  <div class="track">
    <div class="track-title">TRACK TITLE (ORIGINAL MIX)</div>
    <div class="track-artists">ARTIST1 &amp; ARTIST2</div>
  </div>

  <div class="episode">
    <div class="episode-label">EPISODE</div>
    <div class="episode-number">001</div>
  </div>

  <aside class="socials">
    <div class="social-row">
      <span class="social"><span class="social-mark"></span>PAGELINK /ABCDE</span>
      <span class="social"><span class="social-mark"></span>CHIRPNET /ABCDE</span>
    </div>
    <div class="social-row">
      <span class="social"><span class="social-mark"></span>TRELVANO /ABCDE</span>
      <span class="social"><span class="social-mark"></span>WAVEHOLD /ABCDE</span>
    </div>
    <div class="website">WWW.WEBSITE.COM</div>
  </aside>
</main>
</body>
</html>
```